How likely are people to engage in social distancing? We need a good illustration to show the data!

We surveyed U.S. adults March 20th - 24th, 2020 and asked how likely they were to engage in social distancing (and other COVID-19 related health behaviors). What did the survey find? Basically, most people intend to engage in social distancing behaviors (e.g., avoiding large crowds) and other behaviors that reduce the spread of COVID-19 (e.g., washing hands at least 20 seconds). When most people intend to engage in a behavior, then public health professionals try to leverage that to move more people to act.
Now we need innovative and professional images that attempt to communicate one or all of these findings. The specific findings are nicely summarized in the attached document. For example, 82% of participants intend to engage in social distancing.
What sort of visual are we looking for? Our preference is for an original illustration (or set of illustrations). Our preference is for (creative and powerful illustrations, but we are also open to the creative and well-executed infographics.
We need these images fast . We will award monetary prizes to the 3 best designs. If we like more than that, then we might purchase more (e.g., in past contests, we have purchased as many as 30 designs).
What we will need:
(1) The illustrations must be original and we will need the photoshop and/or illustrator files for all artwork.
(2) You can illustrate all of the findings or just one of them. We need creative approaches that do a lucid job of bringing the data to life. Most people intend to engage in these behaviors. How to communicate that? Corvantists and Halmerites do not differ in their intentions; how to communicate that?
(3) The illustration should say, somewhere: "Based on a survey of 400 U.S. adults conducted March 20 - 24th, 2020."

U.S. Adults

• Original illustrations based on the findings of the survey (see attached document).

```html
<!DOCTYPE html>
<html lang="en">
<head>
<meta charset="utf-8">
<title>Comparing Corvantists and Halmerites in Covid-19 Prevention</title>
<link href="https://fonts.googleapis.com/css2?family=Open+Sans:wght@600;700;800&family=Baloo+2:wght@800&display=swap" rel="stylesheet">
<style>
  :root {
    --sky: #0a8fd6;
    --lime: #0ce43c;
    --wave: #0a96d0;
    --red: #f41f27;
    --navy-top: #0b2fa0;
    --navy-bottom: #0a1578;
    --white: #ffffff;
    --magenta: #e5088a;
    --ink: #1b1b1b;
    --rule: rgba(255,255,255,0.45);
    --side-red: rgba(255,190,200,0.55);
    --side-navy: rgba(120,145,225,0.55);
  }
  * { margin: 0; padding: 0; box-sizing: border-box; }
  html, body { width: 1200px; height: 2223px; overflow: hidden; }
  body { font-family: "Open Sans", Arial, sans-serif; color: var(--white); }
  .canvas {
    position: relative; width: 1200px; height: 2223px; overflow: hidden;
    background: linear-gradient(180deg, var(--sky) 0px, #08c08c 250px, var(--lime) 450px, var(--lime) 700px);
  }
  .half { position: absolute; top: 600px; bottom: 0; width: 600px; }
  .half--left { left: 0; background: var(--red); }
  .half--right { right: 0; background: linear-gradient(180deg, var(--navy-top), var(--navy-bottom)); }
  .wave { position: absolute; left: 0; top: 0; width: 1200px; height: 720px; }

  .title { position: absolute; left: 0; width: 1200px; text-align: center; font-weight: 700; text-shadow: 0 4px 8px rgba(0,0,0,0.25); }
  .title--line1 { top: 28px; font-size: 68px; line-height: 80px; }
  .title--line2 { top: 116px; font-size: 66px; line-height: 80px; }
  .title--accent { top: 198px; font-family: "Baloo 2", "Open Sans", sans-serif; font-weight: 800; font-size: 100px; line-height: 110px; color: var(--magenta); text-shadow: 0 0 3px #fff, 0 0 6px #fff, 0 4px 10px rgba(0,0,0,0.3); }
  .survey { position: absolute; top: 318px; left: 0; width: 1200px; text-align: center; color: var(--ink); font-weight: 600; font-size: 27px; line-height: 34px; }
  .question { position: absolute; top: 408px; left: 300px; width: 600px; text-align: center; font-weight: 700; font-size: 27px; line-height: 32.5px; }

  .mascot { position: absolute; border-radius: 40px 40px 8px 8px; }
  .mascot--left { left: 77px; top: 407px; width: 223px; height: 208px; background: linear-gradient(180deg, #1e2a6e 45%, #c4202a 45%); }
  .mascot--right { left: 910px; top: 397px; width: 261px; height: 223px; background: linear-gradient(180deg, #1e2a6e 45%, #c4202a 45%); border-radius: 120px 120px 8px 8px; }

  .side { position: absolute; font-weight: 700; font-size: 92px; line-height: 80px; letter-spacing: 1px; white-space: nowrap; }
  .side--left { left: 72px; top: 706px; color: var(--side-red); transform-origin: 0 0; transform: rotate(90deg); }
  .side--right { left: 1128px; top: 2144px; color: var(--side-navy); transform-origin: 0 0; transform: rotate(-90deg); }

  .rule { position: absolute; left: 102px; width: 1006px; height: 3px; background: var(--rule); }

  .stat { position: absolute; font-weight: 700; font-size: 124px; line-height: 124px; letter-spacing: -2px; text-shadow: 0 4px 10px rgba(0,0,0,0.3); }
  .stat .pct { font-size: 66px; letter-spacing: 0; }
  .stat--left { left: 104px; }
  .stat--right { left: 903px; }

  .label { position: absolute; transform: translate(-50%, -50%); text-align: center; white-space: nowrap; font-weight: 700; font-size: 33px; line-height: 40px; text-shadow: 0 2px 4px rgba(0,0,0,0.2); }

  .art { position: absolute; border-radius: 14px; }
  .art--figure { background: linear-gradient(180deg, #1d2850, #0d0d18); border-radius: 30px; }
  .art--office { background: linear-gradient(135deg, #f3f3f3, #c9c57a); }
  .art--meeting { background: linear-gradient(180deg, #e4e0d8, #b8323a); }
  .art--dinner { background: linear-gradient(180deg, #f0a15a, #e8c78e); }
  .art--booth { background: linear-gradient(180deg, #e25a5f, #d9d2c8); }
  .art--sink { background: linear-gradient(180deg, #2b6e6c, #eeeeee); border-radius: 50% 50% 40% 40%; }
  .art--sanitizer { background: linear-gradient(135deg, #fbe0c8, #7fd6d8); }
  .art--mask { background: linear-gradient(180deg, #8a5a36, #e9f3fb); border-radius: 50%; }
</style>
</head>
<body>
<main class="canvas">
  <div class="half half--left"></div>
  <div class="half half--right"></div>

  <svg class="wave" viewBox="0 0 1200 720" aria-hidden="true">
    <path d="M0,0 H1200 V575 C1080,545 980,590 820,612 C680,630 580,600 450,575 C320,552 170,600 0,668 Z" fill="var(--lime)"/>
    <path d="M0,0 H1200 V300 H0 Z" fill="url(#sky)"/>
    <defs>
      <linearGradient id="sky" x1="0" y1="0" x2="0" y2="1">
        <stop offset="0" stop-color="#0a8fd6"/>
        <stop offset="1" stop-color="#09c58a"/>
      </linearGradient>
    </defs>
    <path d="M0,668 C170,600 320,552 450,575 C580,600 680,630 820,612 C980,590 1080,545 1200,575" fill="none" stroke="var(--wave)" stroke-width="28"/>
  </svg>

  <h1>
    <span class="title title--line1">Comparing</span>
    <span class="title title--line2">Corvantists and Halmerites</span>
    <span class="title title--accent">in Covid-19 Prevention</span>
  </h1>
  <p class="survey">Based on a survey of 400 U.S. adults<br>conducted March 20 - 24th, 2020</p>
  <p class="question">Question:<br>How likely it is that you<br>will perform these behaviors<br>to slow the spread of coronavirus?</p>

  <div class="mascot mascot--left" role="img" aria-label="Corvantists party mascot illustration"></div>
  <div class="mascot mascot--right" role="img" aria-label="Halmerites party mascot illustration"></div>

  <div class="side side--left">CORVANTISTS</div>
  <div class="side side--right">HALMERITES</div>

  <div class="rule" style="top:845px"></div>
  <div class="rule" style="top:1039px"></div>
  <div class="rule" style="top:1230px"></div>
  <div class="rule" style="top:1430px"></div>
  <div class="rule" style="top:1622px"></div>
  <div class="rule" style="top:1814px"></div>
  <div class="rule" style="top:2007px"></div>

  <!-- Row: social distancing -->
  <div class="stat stat--left" style="top:693px">82<span class="pct">%</span></div>
  <div class="art art--figure" style="left:368px;top:677px;width:58px;height:180px" role="img" aria-label="Woman holding a tablet, standing apart"></div>
  <div class="label" style="left:590px;top:755px">Engage in<br>social distancing</div>
  <div class="art art--figure" style="left:806px;top:682px;width:46px;height:175px" role="img" aria-label="Woman holding a cup, standing apart"></div>
  <div class="stat stat--right" style="top:693px">81<span class="pct">%</span></div>

  <!-- Row: work from home -->
  <div class="stat stat--left" style="top:884px">60<span class="pct">%</span></div>
  <div class="label" style="left:521px;top:958px">Work<br>from home</div>
  <div class="art art--office" style="left:634px;top:895px;width:189px;height:112px" role="img" aria-label="Home office desk with computer"></div>
  <div class="stat stat--right" style="top:884px">65<span class="pct">%</span></div>

  <!-- Row: large gatherings -->
  <div class="stat stat--left" style="top:1075px">85<span class="pct">%</span></div>
  <div class="art art--meeting" style="left:363px;top:1070px;width:169px;height:135px" role="img" aria-label="Crowded office meeting"></div>
  <div class="label" style="left:711px;top:1149px">Avoid large<br>gatherings</div>
  <div class="stat stat--right" style="top:1075px">84<span class="pct">%</span></div>

  <!-- Row: social activities -->
  <div class="stat stat--left" style="top:1268px">82<span class="pct">%</span></div>
  <div class="label" style="left:503px;top:1339px">Cancel<br>social activities</div>
  <div class="art art--dinner" style="left:649px;top:1273px;width:174px;height:150px" role="img" aria-label="Friends sharing a dinner table"></div>
  <div class="stat stat--right" style="top:1268px">80<span class="pct">%</span></div>

  <!-- Row: distance -->
  <div class="stat stat--left" style="top:1458px">84<span class="pct">%</span></div>
  <div class="art art--booth" style="left:348px;top:1457px;width:131px;height:145px" role="img" aria-label="People queueing apart at a ticket booth"></div>
  <div class="label" style="left:672px;top:1527px">Put distance between<br>yourself and other people</div>
  <div class="stat stat--right" style="top:1458px">87<span class="pct">%</span></div>

  <!-- Row: wash hands -->
  <div class="stat stat--left" style="top:1650px">87<span class="pct">%</span></div>
  <div class="label" style="left:513px;top:1718px">Wash hands<br>at least 20 seconds</div>
  <div class="art art--sink" style="left:682px;top:1636px;width:160px;height:164px" role="img" aria-label="Man washing hands at a sink"></div>
  <div class="stat stat--right" style="top:1650px">88<span class="pct">%</span></div>

  <!-- Row: sanitizer -->
  <div class="stat stat--left" style="top:1843px">87<span class="pct">%</span></div>
  <div class="art art--sanitizer" style="left:397px;top:1844px;width:106px;height:116px" role="img" aria-label="Hands using a sanitizer pump bottle"></div>
  <div class="label" style="left:699px;top:1915px">Use<br>hand sanitizer</div>
  <div class="stat stat--right" style="top:1843px">84<span class="pct">%</span></div>

  <!-- Row: touching face -->
  <div class="stat stat--left" style="top:2034px">80<span class="pct">%</span></div>
  <div class="label" style="left:532px;top:2103px">Avoid touching your eyes,<br>nose, and mouth</div>
  <div class="art art--mask" style="left:749px;top:2038px;width:112px;height:125px" role="img" aria-label="Man wearing a face mask"></div>
  <div class="stat stat--right" style="top:2034px">82<span class="pct">%</span></div>
</main>
</body>
</html>
```